Meridian Value Bourse (Account) WP Design

We need an Account (Profile) Wordpress design to add to mvb.co.uk.

The design should be based on https://mvb.co.uk/about/. The look and feel of the menu on the left.

The logic, after login the header menu will add another page:

Before Login:
Home / About / Trading / Support /

After Login
Home / About / Trading / Support / Account (Demo) - Logout

When you click on the / Account /

"Account Profile" page is loaded where you can change the settings etc.

"Account Profile" menu on the left should look the same as in / About / (https://mvb.co.uk/about/)

We need the following sub-pages under "Account Profile"

- Profile
- Transfers
- Reports
- Security
- API Key
- Affiliates

Now looking into each page:
-
- Profile (Should be split into individual or business) a user can choose whether how he want to run his account:

[Individual]

Personal Details
First Name:
Middle Name:
Family Name:
Citizenship:
Gender:
DOB:

[Attach File] (Government Issues ID, Passport, Driving License) - Verify

Contact Information
Phone: +44 207 555 0148 - Verify
E-Mail: sample@postvane.example - Verify

Residential Address
Address line 1:
Address line 2:
Address line 3:
City:
Postcode:
Country:

[Attach File] (Utility Bill or Bank Statement) - Verify

[Business]

Company Name:
Registration Number:

Registered Address
Address line 1:
Address line 2:
Address line 3:
City:
Postcode:
Country:

[Attach File] (Certificate of Incorporation) - Verify
[Attach File] (Memorandum & Articles of Association)
[Attach File] (Shareholder Register)

Company Contact Information
Website:

-

- Transfers (Where a user can link a bank account to deposit or withdraw funds from the account)

Transfers

Add a bank account:

Please select the country where beneficiary’s bank is domicile: [Please select]
Please select the currency you wish to make transfers in: [Please select]

Full beneficiary name:
Full beneficiary address:
Beneficiary bank name:
Beneficiary bank address:
Beneficiary Bank Identification Code (BIC)/Routing Code:
Beneficiary IBAN number/account number:

[SAVE]

Deposti funds to MVB Bank Account
Amount of currency to be received e.g. 2345.67 [Please select: USD, EUR, GBP] :
Full beneficiary name: Meridian Value Bourse Limited
Full beneficiary address: Quarrystone Court
7-9 Fenwick Lane
London, United Kingdom
Beneficiary bank name:
Beneficiary bank address:
Beneficiary Bank Identification Code (BIC)/Routing Code: XXXXXXXXXX
Beneficiary IBAN number/account number: XXXXXXXXXXXXXXXXXXXXXXXXXX

Deposit coins to MVB Coin Account
Amount of coins to be received e.g. 2345.67 [Please select: BTC, LTC]:
MVB Coin Account: XXXXXXXXXXXXXXXXXXXXXXXXXXXXX

Applicable charges (?):
[Clear] [Continue]

Withdraw funds from MVB Bank Account
Amount of currency to be sent e.g. 2345.67 [Please select: USD, EUR, GBP] :

Withdraw coins from MVB Coin Account:
Amount of coins to be sent e.g. 2345.67 [Please select: BTC, LTC]:
Please specify you coin account: XXXXXXXXXXXXXXXXXXXXXXXXXXXXX

Applicable charges (?):
[Clear] [Continue]

-

- Reports

TBC
-

- Security

Change Password
Current Password:
New Password:
Confirm New Password:

Enable / Disable : Two-factor Authentication (SMS)

-

- API Key
TBC

-
- Affiliates

Unlimited earning potential!
You'll receive up to 10% commission on all trades made through your affiliate link.

Orbit Referral Circle
Simply apply to our program from your publisher account or click the "Join Now" button below.

Lumenstack.com - Join Now

```html
<!DOCTYPE html>
<html lang="en">
<head>
<meta charset="utf-8">
<title>Account Profile – Meridian Value Bourse</title>
<link rel="stylesheet" href="https://fonts.googleapis.com/css2?family=Arimo:wght@400;700&family=Nunito+Sans:wght@800;900&display=swap">
<style>
:root{
  --brand:#0099d3;
  --brand-dark:#0088bd;
  --panel:#cde8f4;
  --band:#e3e3e3;
  --ink:#111;
  --muted:#555;
  --rule:#9a9a9a;
  --field-border:#c9ced2;
  --white:#fff;
  --btn-dark:#464646;
}
*{box-sizing:border-box;margin:0;padding:0}
html,body{width:1173px;height:1200px;overflow:hidden;background:var(--white)}
body{font-family:"Arimo",Arial,sans-serif;color:var(--ink)}
.page{position:relative;width:1200px;height:1228px;transform:scale(.9775);transform-origin:0 0}
.abs{position:absolute}

/* header */
.top-rule{left:0;top:0;width:1160px;height:1px;background:#bbb}
.brand{left:113px;top:24px;width:150px;font-size:13px;letter-spacing:2px;line-height:18px;color:#333;text-transform:uppercase}
.brand-divider{left:274px;top:14px;width:1px;height:66px;background:#999}
.brand-dot{left:288px;top:27px;width:15px;height:15px;border-radius:50%;border:3px solid #444}
.main-nav{left:290px;top:69px;font-size:12px;color:var(--muted)}
.login{top:42px;height:25px}
.login-field{width:130px;border:1px solid #bbb;font-size:12px;color:#999;padding:5px;background:#fff}
.login-field .hint{position:absolute;right:4px;top:3px;width:18px;height:18px;border-radius:50%;border:1px solid #bbb;font-size:11px;text-align:center;line-height:16px}
.btn-small{height:24px;border-radius:3px;color:#fff;font-size:11px;font-weight:700;text-align:center;line-height:24px}

/* ticker */
.ticker{left:0;top:94px;width:1200px;height:48px;background:var(--brand)}
.coin{left:240px;top:103px;width:31px;height:31px;border-radius:50%;border:3px solid #fff}
.stat{top:101px;color:#fff;border-left:1px solid rgba(255,255,255,.45);padding-left:26px;height:40px}
.stat:first-of-type{border-left:none}
.stat small{display:block;font-size:11px;line-height:14px}
.stat strong{display:block;font-weight:400;font-size:14px;line-height:20px}

/* title band */
.title-band{left:0;top:143px;width:1200px;height:78px;background:var(--band);border-bottom:1px solid #aaa}
.page-title{left:125px;top:167px;font-size:31px;font-weight:700;letter-spacing:.3px}
.mode{left:1083px;top:187px;font-size:12px;font-weight:700;letter-spacing:.8px}

/* sidebar */
.side-nav{left:123px;top:266px;width:221px;list-style:none}
.side-nav li{height:38px;border-bottom:1px solid #777;font-size:15px;line-height:38px;padding-top:2px}
.side-nav li.current{color:var(--brand);font-weight:700}

/* panel */
.panel{left:393px;top:239px;width:785px;height:636px;background:var(--panel);border-radius:4px}
.section-title{font-family:"Nunito Sans",Arial,sans-serif;font-weight:900;font-size:17px;color:var(--brand);letter-spacing:.2px}
.label{font-size:12px;color:#222}
.field{width:205px;height:33px;background:#fff;border:1px solid var(--field-border);border-radius:6px;font-size:12px;font-weight:700;padding:9px 19px;color:#111}
.verify{font-size:12px;font-weight:700}
.verify span{text-decoration:underline}
.attach{width:106px;height:31px;background:var(--brand);color:#fff;font-size:12px;text-align:center;line-height:31px}

/* footer */
.footer{left:0;top:898px;width:1200px;height:330px;background:var(--brand);color:#fff}
.foot-brand{left:123px;top:944px;width:140px;font-size:11px;letter-spacing:2px;line-height:20px;text-transform:uppercase;color:#fff}
.foot-divider{left:269px;top:938px;width:1px;height:70px;background:rgba(255,255,255,.7)}
.foot-dot{left:282px;top:950px;width:13px;height:13px;border-radius:50%;border:3px solid #fff}
.copy{left:123px;top:1023px;font-size:11px;line-height:14px}
.foot-head{font-size:22px;font-weight:700;top:939px}
.foot-links{list-style:none;font-size:12px;line-height:15px;top:978px}
.social{top:978px;width:28px;height:28px;border-radius:50%;background:#fff}
.tagline{left:518px;top:1108px;width:572px;height:76px;background:linear-gradient(90deg,rgba(255,255,255,.08),rgba(255,255,255,.2));border-radius:4px}
</style>
</head>
<body>
<div class="page">

<header>
  <div class="abs top-rule"></div>
  <div class="abs brand">Meridian Value Bourse</div>
  <div class="abs brand-divider"></div>
  <div class="abs brand-dot"></div>
  <nav class="abs main-nav">Home · About · Trading · Support</nav>

  <div class="abs login login-field" style="left:696px">Email<span class="hint">?</span></div>
  <div class="abs login login-field" style="left:836px">Password<span class="hint">?</span></div>
  <div class="abs login btn-small" style="left:976px;width:55px;background:var(--btn-dark)">Log In</div>
  <div class="abs login btn-small" style="left:1036px;width:55px;background:var(--brand)">Sign Up</div>
</header>

<section class="abs ticker"></section>
<div class="abs coin"></div>
<div class="abs stat" style="left:258px;border-left:none"><small>Current Price</small><strong>$444.13</strong></div>
<div class="abs stat" style="left:372px"><small>Daily Change</small><strong>-9.54 <span style="font-size:11px">↘2.10%</span></strong></div>
<div class="abs stat" style="left:497px"><small>Day's Range</small><strong>$440.00 - $457.30</strong></div>
<div class="abs stat" style="left:665px"><small>Today's Open</small><strong>$453.57</strong></div>
<div class="abs stat" style="left:783px"><small>24h Volume</small><strong>7194 BTC</strong></div>

<div class="abs title-band"></div>
<h1 class="abs page-title">Account Profile</h1>
<div class="abs mode">BUSINESS</div>

<ul class="abs side-nav">
  <li class="current">Profile</li>
  <li>Transfers</li>
  <li>Reports</li>
  <li>Security</li>
  <li>API Key</li>
  <li>Affiliates</li>
</ul>

<main class="abs panel"></main>

<h2 class="abs section-title" style="left:420px;top:267px">Business Details</h2>
<div class="abs label" style="left:421px;top:319px">Company Name:</div>
<div class="abs field" style="left:565px;top:307px"></div>
<div class="abs label" style="left:421px;top:364px">Registration Number:</div>
<div class="abs field" style="left:565px;top:350px"></div>

<h2 class="abs section-title" style="left:803px;top:267px">Company Contact Information</h2>
<div class="abs label" style="left:808px;top:319px">Phone:</div>
<div class="abs field" style="left:868px;top:307px">+44 207 555 0148</div>
<div class="abs verify" style="left:1087px;top:317px">- <span>Verify</span></div>
<div class="abs label" style="left:808px;top:364px">E-Mail:</div>
<div class="abs field" style="left:868px;top:353px;padding-top:7px">sample@postvane.example</div>
<div class="abs verify" style="left:1087px;top:360px">- <span>Verify</span></div>
<div class="abs label" style="left:808px;top:409px">Website:</div>
<div class="abs field" style="left:868px;top:399px">sample@postvane.example</div>
<div class="abs verify" style="left:1087px;top:409px">- <span>Verify</span></div>

<h2 class="abs section-title" style="left:428px;top:489px">Registered Address</h2>
<div class="abs label" style="left:429px;top:545px">Address line 1:</div>
<div class="abs field" style="left:565px;top:536px"></div>
<div class="abs label" style="left:429px;top:590px">Address line 2:</div>
<div class="abs field" style="left:565px;top:581px"></div>
<div class="abs label" style="left:429px;top:635px">Address line 3:</div>
<div class="abs field" style="left:565px;top:626px"></div>
<div class="abs label" style="left:429px;top:680px">City:</div>
<div class="abs field" style="left:565px;top:670px"></div>
<div class="abs label" style="left:429px;top:725px">Postcode:</div>
<div class="abs field" style="left:565px;top:715px"></div>
<div class="abs label" style="left:429px;top:770px">Country:</div>
<div class="abs field" style="left:565px;top:760px"></div>

<h2 class="abs section-title" style="left:810px;top:489px">File Attachments</h2>
<div class="abs label" style="left:812px;top:566px">Certificate of Incorporation</div>
<div class="abs attach" style="left:975px;top:557px">Attach File</div>
<div class="abs verify" style="left:1097px;top:565px">- <span>Verify</span></div>
<div class="abs label" style="left:812px;top:632px;line-height:12px">Memorandum &amp; Articles<br>of Association</div>
<div class="abs attach" style="left:973px;top:625px">Attach File</div>
<div class="abs verify" style="left:1097px;top:632px">- <span>Verify</span></div>
<div class="abs label" style="left:812px;top:703px">Shareholder Register</div>
<div class="abs attach" style="left:973px;top:695px">Attach File</div>
<div class="abs verify" style="left:1097px;top:703px">- <span>Verify</span></div>

<footer class="abs footer"></footer>
<div class="abs foot-brand">Meridian Value Bourse</div>
<div class="abs foot-divider"></div>
<div class="abs foot-dot"></div>
<div class="abs copy" style="color:#fff">© 2014 Meridian Value Bourse.<br>All rights reserved</div>

<h3 class="abs foot-head" style="left:463px;color:#fff">ABOUT US</h3>
<ul class="abs foot-links" style="left:463px;color:#fff">
  <li>Rulebook</li><li>Trading Fees</li><li>Partners</li><li>Security</li><li>Terms of Service</li><li>Privacy Policy</li><li>Latest News</li>
</ul>
<h3 class="abs foot-head" style="left:719px;color:#fff">SUPPORT</h3>
<ul class="abs foot-links" style="left:719px;color:#fff">
  <li>What is Bitcoin?</li><li>How to buy a bitcoin?</li><li>How to sell a bitcoin?</li>
</ul>
<h3 class="abs foot-head" style="left:949px;color:#fff">FOLLOW MVB</h3>
<div class="abs social" style="left:949px"></div>
<div class="abs social" style="left:989px"></div>
<div class="abs social" style="left:1030px"></div>
<div class="abs social" style="left:1070px"></div>

<div class="abs tagline" role="img" aria-label="Hand-lettered white script slogan: Change the world one bitcoin at a time"></div>

</div>
</body>
</html>
```